MY BEST MARKETING TOOL 8 PAGE FULL COLOR BOOKLET TO PHYSICIANS

I HAVE CORRECT DATA IN RIGHT PLACES. NEED HELP WITH FINISHING TOUCHES TO MAKE IT LOOK PROFESSIONAL AND GET IT PRINT READY. I HAVE USED CANVA TO GET THIS FAR. SO IF I NEED TO SHARE CANVA WITH YOU, HAPPY TO DO SO. THESE BOOKLETS WILL BE USED IN MARKETING. AUDIENCE IS DOCTORS. I WANT INFO TO BE CLEAR AND EASY TO FOLLOW.
Updates

MY FAVORITE COLORS ARE NAVY BLUE, COLUMBIA (SKY BLUE), LIGHT GRAY, SILVER, AND WHITE. THINK THESE SHOULD BE BASIC COLOR RANGE.

TRY TO USE LARGER TEXT PLEASE.

WEBSITE FOR BUSINESS---------------CAREHALO918.COM

Target Market(s)

FAMILY MEDICINE PHYSICIANS

Industry/Entity Type

MEDICAL

Font styles to use
Other font styles liked:
• CEREBRI, CODE PRO

Colors
0054AA
0677BA
7BADD7
CADEEF
E8F1F8

Requirements
Must have
• CLEAN, NEAT, CLEAR, BUT VERY PROFESSIONAL LOOK
Nice to have
• IMPROVE LAYOUT/GRAPHICS/TABLES/BOXES/DIFFERENT COLOR TEXT IN PLACES, I LIKE PAGES WITH FULL BORDER OR SPLIT PAGE INTO 2 WITH SOME GRAPHIC. ETC.
Should not have
• DONT WANT FANCY. ALL PROFESSIONAL

```html
<!DOCTYPE html>
<html lang="en">
<head>
<meta charset="utf-8">
<title>CareHalo – Physician Booklet Spreads</title>
<link rel="stylesheet" href="https://fonts.googleapis.com/css2?family=Montserrat:wght@300;400;500;600;700&display=swap">
<style>
  :root{
    --board:#7a8a96;
    --navy:#26418f;
    --white:#ffffff;
    --mist:#e6edf5;
    --chart-bg:#ececec;
    --rule:#c9d3e6;
    --ink:#1d2b55;
    --photo-a:#c9c3b8;
    --photo-b:#8a9bb5;
    --silver-a:#f2f2f2;
    --silver-b:#bfc3c8;
  }
  *{box-sizing:border-box;margin:0;padding:0}
  html,body{width:1200px;height:849px;overflow:hidden;background:var(--board)}
  body{font-family:"Montserrat",Arial,sans-serif;color:var(--white)}
  .board{position:relative;width:1200px;height:849px;background:var(--board)}

  /* each page is authored at 420×594 and scaled to fit the board */
  .page{position:absolute;width:420px;height:594px;overflow:hidden;
        transform:scale(.5226);transform-origin:0 0;background:var(--white);
        box-shadow:14px 16px 22px rgba(30,40,55,.35)}
  .p1{left:76.3px;top:81.5px}
  .p2{left:352.2px;top:81.5px}
  .p3{left:628.2px;top:81.5px}
  .p4{left:904.1px;top:81.5px}
  .p5{left:76.3px;top:456.2px}
  .p6{left:352.2px;top:456.2px}
  .p7{left:628.2px;top:456.2px}
  .p8{left:904.1px;top:451px}

  .abs{position:absolute}
  .navy{background:var(--navy)}
  .mist{background:var(--mist)}
  .photo{position:absolute}

  /* cover */
  .cover{background:var(--navy);text-align:center}
  .cover .brand{position:absolute;top:180px;left:0;width:100%;font-size:31px;font-weight:300;letter-spacing:2px}
  .cover .brand-mark{display:inline-block;width:14px;height:14px;background:var(--white);margin-right:10px;vertical-align:3px}
  .cover .divider{position:absolute;top:248px;left:115px;width:190px;height:1px;background:#b8c3dd}
  .cover .tagline{position:absolute;top:274px;left:0;width:100%;font-size:15px;letter-spacing:4px;line-height:18px}
  .cover .motto{position:absolute;top:472px;left:0;width:100%;font-size:17.5px;letter-spacing:2.5px}

  /* founder */
  .founder-photo{left:0;top:0;width:311px;height:376px;background:linear-gradient(160deg,var(--photo-a),var(--photo-b))}
  .founder-box{left:143px;top:339px;width:277px;height:204px;background:var(--navy);padding:29px 21px 0 21px;
               font-size:10.6px;line-height:14.9px;text-align:justify}

  /* programs */
  .prog-top{left:0;top:0;width:420px;height:258px;background:var(--navy);padding:34px 25px 0 25px}
  .prog-top p{font-size:10.6px;line-height:13.4px}
  .prog-top h3{font-size:10.6px;font-weight:700;margin-top:17px;margin-bottom:5px}
  .prog-list{list-style:none;font-size:10.2px;line-height:20px}
  .prog-list li::before{content:"•";margin-right:8px}
  .prog-list .prog-name{font-weight:700}
  .chart-area{left:0;top:258px;width:420px;height:220px;background:var(--chart-bg)}
  .chart-title{position:absolute;top:8px;left:0;width:100%;text-align:center;color:var(--navy);font-size:12px;font-weight:700}
  .chart-area svg{position:absolute;left:0;top:0}
  .prog-bottom{left:0;top:478px;width:420px;height:116px;background:var(--navy);padding:10px 25px 0 25px}
  .prog-bottom p{font-size:8.6px;line-height:11.4px}
  .prog-bottom .goal{font-size:15.5px;font-weight:700;margin-top:7px;line-height:20px}

  /* CCM / BHI */
  .ccm-photo{left:0;top:0;width:420px;height:275px;background:linear-gradient(120deg,#3a3d42 0%,#9a9ea4 35%,#eceeef 70%,#f7f7f7 100%)}
  .ccm-body{left:0;top:275px;width:420px;height:319px;background:var(--navy);padding:18px 25px 0 25px}
  .page-title{font-size:19.5px;font-weight:700;line-height:25.5px}
  .ccm-body .lead{font-size:10.4px;line-height:13.4px;margin-top:10px;width:310px}
  .short-rule{width:42px;height:3px;background:var(--white);margin:22px 0 16px}
  .dot-list{list-style:none;font-size:10.4px;line-height:13px}
  .dot-list li{position:relative;padding-left:13px;margin-bottom:7px}
  .dot-list li::before{content:"•";position:absolute;left:0}

  /* RPM */
  .rpm-band{left:109px;top:0;width:311px;height:594px;background:var(--navy)}
  .rpm-photo{left:50px;top:62px;width:370px;height:232px;background:linear-gradient(135deg,var(--silver-a),var(--silver-b));border-radius:6px}
  .rpm-text{left:151px;top:330px;width:248px}
  .rpm-text .short-rule{margin:14px 0 18px}
  .rpm-text p{font-size:8.9px;line-height:11.6px;margin-bottom:6px}

  /* why */
  .why-head{left:25px;top:48px;color:var(--navy)}
  .why-head h2{font-size:23.5px;font-weight:700}
  .why-head .sub{font-size:15.5px;letter-spacing:2px;margin-top:12px;font-weight:400}
  .why-left{left:0;top:153px;width:209px;height:441px;background:var(--navy);padding:24px 14px 0 25px}
  .why-right{left:209px;top:153px;width:211px;height:441px;background:var(--mist);padding:24px 16px 0 13px;color:var(--ink)}
  .why-left p,.why-right p{font-size:10.3px;line-height:13.4px;margin-bottom:13px}
  b{font-weight:700}

  /* start-up */
  .start-top{left:0;top:0;width:420px;height:174px;background:var(--navy);padding:46px 25px 0 25px}
  .start-top h2{font-size:23.5px;font-weight:700}
  .start-top p{font-size:10.6px;line-height:13.4px;text-align:justify;margin-top:16px}
  .start-body{left:0;top:174px;width:420px;height:420px;background:var(--mist);color:var(--navy);text-align:center}
  .profit{position:absolute;top:46px;width:100%;font-size:16px;font-weight:700;text-decoration:underline;text-underline-offset:3px}
  .phase{position:absolute;width:100%}
  .phase h4{display:inline-block;font-size:16px;font-weight:700;padding:0 8px 7px;border-bottom:1px solid var(--navy)}
  .phase p{font-size:9.2px;color:var(--ink);margin-top:15px}
  .phase-build{top:116px}
  .phase-manage{top:207px}
  .paid-pill{position:absolute;left:67px;top:336px;width:285px;height:34px;border-radius:17px;background:var(--navy);
             color:var(--white);font-size:11.3px;font-weight:700;line-height:34px}

  /* testimonials */
  .happy-band{left:0;top:0;width:92px;height:594px;background:var(--navy)}
  .happy-title{left:169px;top:76px;color:var(--navy);font-size:23.5px;font-weight:700;line-height:30px}
  .patient-photo{left:33px;width:118px;height:123px;background:linear-gradient(180deg,#d9d9d9,#6e6e6e)}
  .patient{left:169px;width:227px;color:var(--ink)}
  .patient .name{font-size:11.5px;font-weight:700;color:var(--navy);border-bottom:1px solid var(--ink);padding-bottom:2px}
  .patient .role{font-size:7.6px;margin-top:6px}
  .patient .bio{font-size:6.4px;line-height:8.4px;margin-top:10px;text-align:justify}
</style>
</head>
<body>
<main class="board">

  <!-- page 1: cover -->
  <section class="page p1 cover">
    <div class="brand"><span class="brand-mark"></span>CAREHALO</div>
    <div class="divider"></div>
    <div class="tagline">CHRONIC CARE<br>EXPERTS</div>
    <div class="motto">SAVING LIVES 24/7</div>
  </section>

  <!-- page 2: founder -->
  <section class="page p2">
    <div class="photo founder-photo" role="img" aria-label="Family portrait of the founder with his family on a beach"></div>
    <div class="abs founder-box">
      Daniel Prewitt, RN, BSN started CareHalo One, LLC in 2022 to provide Chronic Care Services with the mission to help people stay at home and out of the hospital. His first job was an orderly in the hospital at age 17. In the past 35 years, he has successfully started, grown, and sold a Physical Therapy clinic, a Home Medical Equipment company, and a Sleep Lab. From 2015 to 2022, he worked as a Critical Care Travel Nurse in 5 states.
    </div>
  </section>

  <!-- page 3: programs -->
  <section class="page p3">
    <div class="abs prog-top">
      <p>CMS created Chronic Care Management (CCM) in 2015 to improve quality of healthcare and reduce hospital visits which lowers overall healthcare related costs. Statistics show up to 50% cost reduction in patients enrolled in CCM.</p>
      <h3>Our Programs (Enrollment % of your total Medicare Population)</h3>
      <ul class="prog-list">
        <li class="prog-name">Chronic Care Management</li>
        <li>2 Chronic Conditions <b>(80% Enrollment)</b></li>
        <li class="prog-name">Remote Patient Monitoring (RPM)</li>
        <li>BP, Pulse Ox, Glucometer, Scale <b>(70% Enrollment)</b></li>
        <li class="prog-name">Behavioral Health (BHI)</li>
        <li>1 Mental Health condition <b>(60% Enrollment)</b></li>
      </ul>
    </div>
    <div class="abs chart-area">
      <div class="chart-title">CHRONIC CONDITION PREVALENCE &gt; 65 YRS</div>
      <svg width="420" height="220" viewBox="0 0 420 220" font-family="Montserrat, Arial, sans-serif" font-size="5" fill="#6b6b6b">
        <g stroke="#cfcfcf" stroke-width="0.8">
          <line x1="120" y1="32" x2="120" y2="200"/>
          <line x1="188" y1="32" x2="188" y2="200"/>
          <line x1="256" y1="32" x2="256" y2="200"/>
          <line x1="323" y1="32" x2="323" y2="200"/>
        </g>
        <g fill="#26418f">
          <rect x="120" y="32" width="195" height="5"/>
          <rect x="120" y="49" width="136" height="5"/>
          <rect x="120" y="66" width="116" height="5"/>
          <rect x="120" y="84" width="116" height="5"/>
          <rect x="120" y="101" width="116" height="5"/>
          <rect x="120" y="118" width="89" height="5"/>
          <rect x="120" y="136" width="89" height="5"/>
          <rect x="120" y="153" width="68" height="5"/>
          <rect x="120" y="170" width="61" height="5"/>
          <rect x="120" y="188" width="61" height="5"/>
        </g>
        <g text-anchor="end">
          <text x="117" y="37">HTN</text>
          <text x="117" y="54">HLD</text>
          <text x="117" y="71">CKD</text>
          <text x="117" y="89">OBESITY</text>
          <text x="117" y="106">MEMORY</text>
          <text x="117" y="123">DIABETES</text>
          <text x="117" y="141">PAIN</text>
          <text x="117" y="158">CANCER</text>
          <text x="117" y="175">COPD</text>
          <text x="117" y="193">CHF</text>
        </g>
        <g text-anchor="middle">
          <text x="120" y="208">0%</text>
          <text x="188" y="208">25%</text>
          <text x="256" y="208">50%</text>
          <text x="323" y="208">75%</text>
        </g>
      </svg>
    </div>
    <div class="abs prog-bottom">
      <p>CareHalo maximizes access to all available resources, minimizes barriers to compliance, and encourages positive lifestyle choices. Our nurses are personal advocates for your clients.</p>
      <div class="goal">Our # 1 Goal is to prevent MIs and CVAs.</div>
    </div>
  </section>

  <!-- page 4: CCM / BHI -->
  <section class="page p4">
    <div class="photo ccm-photo" role="img" aria-label="Office phone with a call-center headset on a white desk"></div>
    <div class="abs ccm-body">
      <h2 class="page-title">CCM- Chronic Care<br>BHI-Behavioral Health</h2>
      <p class="lead">A Registered Nurse will be accessible by phone 24 / 7 for addressing patient needs such as assessments, refills, education, and expediting sick visits.</p>
      <div class="short-rule"></div>
      <ul class="dot-list">
        <li>Assisting in referrals to specialists and home care services.</li>
        <li>Assisting with social services, transportation, and medical equipment and supplies.</li>
        <li>Scheduling any preventive care needed.</li>
        <li>Providing nutritional education and supporting positive lifestyle changes.</li>
      </ul>
    </div>
  </section>

  <!-- page 5: RPM -->
  <section class="page p5">
    <div class="abs rpm-band"></div>
    <div class="photo rpm-photo" role="img" aria-label="Remote monitoring devices: blood pressure cuff, glucometer, pulse oximeter and scale"></div>
    <div class="abs rpm-text">
      <h2 class="page-title">RPM- Remote Patient<br>Monitoring</h2>
      <div class="short-rule"></div>
      <p>Remote monitoring devices are provided which track blood pressure, weight, oxygen, glucose and automatically upload to our software sending us alerts in real time. Alerts are monitored and addressed 24/7.</p>
      <p>RN's provide critical thinking and assessments for patients around the clock. If intervention is needed we notify provider with data for new meds, sick visit, or referral to urgent/emergent care. Notifications to providers and staff are sent as telephone encounters via ChartLink for seamless communication from nurses to provider.</p>
    </div>
  </section>

  <!-- page 6: why -->
  <section class="page p6">
    <div class="abs why-head">
      <h2>Why CareHalo?</h2>
      <div class="sub">WE STAFF LOCAL RN’S</div>
    </div>
    <div class="abs why-left">
      <p>CareHalo guarantees a dedicated team of <b>Critical Care RN’s, LPN’s and Medical Assistants.</b> We continue to build our team with the most <b>experienced and passionate</b> advocates to ensure the absolute best service for your clients.</p>
      <p>CareHalo bridges the gap between clinical and home environments. We prioritize <b>following up</b> and following through which results in better coordination of care and the best possible outcomes.</p>
      <p>We maintain 100% compliance with <b>Annual Wellness Visits.</b> Maintaining the <b>highest standards</b> is a priority for our team and is what sets us apart from other Chronic Care Providers.</p>
    </div>
    <div class="abs why-right">
      <p>Using ChartLink guarantees seamless integration into your practice. The GOAL is for clients to call CCM 24/7 phone instead of main office for all needs. <b>This eliminates non-billable staff time.</b></p>
      <p>Our <b>average monthly reimbursement is $125 greater than the national average</b> because we believe in spending as much time with our patients as needed.</p>
      <p>Our daily average is <b>70 outgoing calls and 40 incoming calls.</b> We typically respond to <b>65</b> RPM alerts and <b>10</b> Telephone Encounters daily. We send several patients to ER weekly.</p>
    </div>
  </section>

  <!-- page 7: start-up costs -->
  <section class="page p7">
    <div class="abs start-top">
      <h2>Start Up Costs</h2>
      <p>CareHalo covers all upfront costs including ChartLink, clinical and billing staff, providers’ staff orientation, and all marketing materials (mass email, magnetic business cards with 24/7 phone number, brochures, posters, and webpage for your current website). RPM devices will cost over $100,00</p>
    </div>
    <div class="abs start-body">
      <div class="profit">Monthly Net Profit per 1000 clients</div>
      <div class="phase phase-build">
        <h4>Building Phase</h4>
        <p>First 6 months $50,000 ($50 per patient)</p>
      </div>
      <div class="phase phase-manage">
        <h4>Management Phase</h4>
        <p>After 6 months $100,000 ($100 per patient)</p>
      </div>
      <div class="paid-pill">CareHalo gets paid after Medicare pays you!</div>
    </div>
  </section>

  <!-- page 8: testimonials -->
  <section class="page p8">
    <div class="abs happy-band"></div>
    <h2 class="abs happy-title">Happy<br>Patients...</h2>

    <div class="photo patient-photo" style="top:135px" role="img" aria-label="Black and white portrait of a patient"></div>
    <div class="abs patient" style="top:181px">
      <div class="name">Arlo Benton</div>
      <div class="role">Product Designer</div>
      <div class="bio">Booklets are printed materials with four or more pages, containing details about a business, event, product, promotion, etc. They are also known as catalogs or pamphlets, and are usually created to communicate a message to a wide variety of audiences.</div>
    </div>

    <div class="photo patient-photo" style="top:265px" role="img" aria-label="Black and white portrait of a patient"></div>
    <div class="abs patient" style="top:309px">
      <div class="name">Marcus Feld</div>
      <div class="role">Marketer</div>
      <div class="bio">Booklets are printed materials with four or more pages, containing details about a business, event, product, promotion, etc. They are also known as catalogs or pamphlets, and are usually created to communicate a message to a wide variety of audiences.</div>
    </div>

    <div class="photo patient-photo" style="top:397px" role="img" aria-label="Black and white portrait of a patient"></div>
    <div class="abs patient" style="top:444px">
      <div class="name">Lena Kovac</div>
      <div class="role">Graphic Designer</div>
      <div class="bio">Booklets are printed materials with four or more pages, containing details about a business, event, product, promotion, etc. They are also known as catalogs or pamphlets, and are usually created to communicate a message to a wide variety of audiences.</div>
    </div>
  </section>

</main>
</body>
</html>
```